Pinecrest Premier Motors *

Professional business cards for our auto wholesale dealership.

Target Market(s)

New and used cars sales managers and middle class to higher end private party buyers.

Industry/Entity Type

Automotive

Contact Information for Business Card

Pinecrest Premier Motors
Marcus T Holloran
Owner
(555) 014-3862
pineprem@mailvista.example
Dealer Lic # 48265

Logo Text

Pinecrest Premier Motors, Pine Prem Motors, PPM, etc

Font styles to use
Serif
Sans Serif

Colors

Designer to choose colors to be used in the design.

Requirements
Must have
• A professional, but not pretentious, look
Nice to have
• It might be nice to see "PPM" in a shape form i.e. circle, triangle, etc in the corner or background somehwere
Should not have
• bright "girly" colors

```html
<!DOCTYPE html>
<html lang="en">
<head>
<meta charset="utf-8">
<title>Pinecrest Premier Motors — Business Cards</title>
<link href="https://fonts.googleapis.com/css2?family=Oswald:wght@500;600&family=Open+Sans:wght@400;600&display=swap" rel="stylesheet">
<style>
  :root {
    --backdrop: #2f2a27;
    --card: #0d0d0d;
    --crimson: #c8193f;
    --green: #2f8f2a;
    --silver: #c9c9c9;
    --white: #f1f1f1;
    --shadow: rgba(0,0,0,0.55);
  }
  * { margin: 0; padding: 0; box-sizing: border-box; }
  html, body {
    width: 1200px; height: 900px; overflow: hidden;
    background: var(--backdrop);
  }
  .sheet {
    position: relative; width: 1200px; height: 900px;
    display: flex; align-items: center; justify-content: center; gap: 60px;
  }
  .card {
    position: relative; width: 525px; height: 300px;
    background: var(--card);
    box-shadow: 0 14px 30px var(--shadow);
  }
  .wordmark {
    font-family: "Oswald", sans-serif; font-weight: 600;
    text-transform: uppercase; letter-spacing: 0.5px; white-space: nowrap;
  }
  /* Front */
  .card-front .wordmark {
    position: absolute; top: 78px; right: 40px;
    font-size: 31px; color: var(--crimson);
  }
  .card-front .rule {
    position: absolute; top: 150px; left: 215px; right: 30px;
    height: 2px; background: var(--crimson);
  }
  .contact {
    position: absolute; top: 166px; right: 30px;
    font-family: "Open Sans", sans-serif; font-size: 14px;
    color: var(--white); text-align: right; line-height: 22px;
    text-transform: uppercase;
  }
  .contact-line { display: flex; align-items: center; justify-content: flex-end; gap: 6px; }
  .contact-line svg { width: 11px; height: 11px; fill: var(--crimson); }
  .person {
    position: absolute; left: 36px; bottom: 34px;
    font-family: "Open Sans", sans-serif; text-transform: uppercase;
  }
  .person-name {
    font-family: "Oswald", sans-serif; font-weight: 600;
    font-size: 21px; color: var(--crimson); letter-spacing: 0.5px;
  }
  .person-role { font-size: 14px; color: var(--green); margin-top: 2px; }
  .person-licence { font-size: 14px; color: var(--crimson); margin-top: 4px; }
  .person-licence .number { color: var(--white); font-weight: 600; }
  /* Back */
  .card-back {
    display: flex; align-items: center; justify-content: center;
  }
  .card-back .wordmark { font-size: 34px; color: var(--silver); }
</style>
</head>
<body>
<main class="sheet">
  <section class="card card-front" aria-label="Business card front">
    <div class="wordmark">Pinecrest Premier Motors</div>
    <div class="rule"></div>
    <div class="contact">
      <div class="contact-line">(555) 014-3862
        <svg viewBox="0 0 24 24" aria-hidden="true"><path d="M6.6 10.8a15 15 0 006.6 6.6l2.2-2.2a1 1 0 011-.25 11.4 11.4 0 003.6.57 1 1 0 011 1V20a1 1 0 01-1 1A17 17 0 013 4a1 1 0 011-1h3.5a1 1 0 011 1 11.4 11.4 0 00.57 3.6 1 1 0 01-.25 1z"/></svg>
      </div>
      <div class="contact-line">pineprem@mailvista.example
        <svg viewBox="0 0 24 24" aria-hidden="true"><path d="M2 5h20v14H2z M2 5l10 8 10-8" fill="var(--crimson)"/><path d="M2 5l10 8 10-8" fill="none" stroke="#0d0d0d" stroke-width="2"/></svg>
      </div>
    </div>
    <div class="person">
      <div class="person-name">Marcus T Holloran</div>
      <div class="person-role">Owner</div>
      <div class="person-licence">Dealer Lic <span class="number"># 48265</span></div>
    </div>
  </section>
  <section class="card card-back" aria-label="Business card back">
    <div class="wordmark">Pinecrest Premier Motors</div>
  </section>
</main>
</body>
</html>
```